White Paper and One-Page Advertisement for TELVAMORE-QX

I need both documents to be better formatted and designed so they look professional, not something someone with mediocre word skills put together. They will go out to 1000s of industry professionals, and they need to look sharp. I need them to have my company's color palate logo, and branding on it similar to how it is now, but better. Please do not change any of the written content, but it can be arranged in any other format you think is better. Smart art and things i've already used can be omitted in favor of better designs. The developer is free to use their creativity. White paper should not be longer than the three pages unless necessary.

Target Market(s)

Life Sciences supply chain professionals

Colors
33b8a4
0592cd
9bcb3c
fbee3e
3277b5

Requirements
Must have
• Must be professional looking and not look like something done in word. Please use the color palate as seen on the documents.
Should not have
• Any changes to the written content.

```html
<!DOCTYPE html>
<html lang="en">
<head>
<meta charset="utf-8">
<title>TELVAMORE-QX — One-Page Advertisement</title>
<link rel="stylesheet" href="https://fonts.googleapis.com/css2?family=Roboto:wght@400;500&family=Roboto+Condensed:wght@700&display=swap">
<style>
  :root {
    --ink: #3a3a3a;
    --brand-green: #1c7a5e;
    --brand-lime: #9bcb3c;
    --brand-teal: #33b8a4;
    --heading-blue: #0a57a0;
    --footer-blue: #0b5aa3;
    --photo-warm: #8a5a3a;
    --photo-teal: #2f5d63;
    --paper: #ffffff;
  }
  * { box-sizing: border-box; margin: 0; padding: 0; }
  html, body { width: 907px; height: 1200px; overflow: hidden; background: var(--paper); }
  body { font-family: "Roboto", Arial, sans-serif; color: var(--ink); position: relative; }

  .masthead { position: absolute; top: 0; left: 0; width: 907px; height: 161px;
    display: flex; align-items: center; justify-content: center; gap: 14px; padding-top: 50px; }
  .masthead-dot { width: 26px; height: 26px; border-radius: 50%; background: var(--brand-lime); }
  .brand-name { font-family: "Roboto Condensed", Arial, sans-serif; font-weight: 700;
    font-size: 40px; letter-spacing: 1px; color: var(--brand-green); }

  .hero { position: absolute; top: 161px; left: 0; width: 907px; height: 264px;
    background: linear-gradient(100deg, #6e4a2e 0%, #c9a46a 22%, #d9cfc0 40%, var(--photo-teal) 62%, #3b6a70 80%, var(--photo-warm) 100%); }
  .hero-rule { position: absolute; top: 425px; left: 0; width: 907px; height: 8px; background: var(--brand-lime); }

  .section-tag { position: absolute; left: 64px; width: 227px; height: 36px; border-radius: 4px;
    font-family: "Roboto Condensed", Arial, sans-serif; font-weight: 700; font-size: 24px;
    color: #fff; padding-left: 18px; line-height: 36px; }
  .tag-platform { top: 450px; background: var(--heading-blue); }
  .tag-benefits { top: 724px; background: var(--brand-teal); }
  .tag-promise { top: 1010px; background: var(--brand-lime); }

  .checklist { position: absolute; left: 0; width: 907px; list-style: none; }
  .checklist li { position: absolute; left: 64px; width: 810px; font-size: 15.5px; line-height: 19px; }
  .checklist svg { position: absolute; left: -33px; top: 2px; width: 14px; height: 14px; }

  .footer { position: absolute; left: 0; top: 1128px; width: 907px; height: 72px; background: var(--footer-blue);
    display: flex; align-items: center; justify-content: center; gap: 52px; color: #fff; font-size: 16.5px; }
  .footer-item { display: flex; align-items: center; gap: 12px; }
  .footer-item svg { width: 13px; height: 13px; }
</style>
</head>
<body>
  <header class="masthead">
    <span class="masthead-dot"></span>
    <span class="brand-name">TELVAMORE-QX</span>
  </header>

  <div class="hero" role="img" aria-label="Photograph of people in traditional dress helping each other at a ceremony"></div>
  <div class="hero-rule"></div>

  <svg width="0" height="0" style="position:absolute">
    <symbol id="tick-box" viewBox="0 0 14 14">
      <rect x="1" y="3" width="10" height="10" fill="none" stroke="#444" stroke-width="1.3"/>
      <path d="M3.5 7.5 L6 10 L13 1.5" fill="none" stroke="#444" stroke-width="1.6"/>
    </symbol>
  </svg>

  <div class="section-tag tag-platform">OUR PLATFORM</div>
  <ul class="checklist">
    <li style="top:504px"><svg><use href="#tick-box"/></svg>A multi-vendor marketplace for the life science community to transact pre-market and after-market materials and equipment</li>
    <li style="top:561px"><svg><use href="#tick-box"/></svg>Researchers, manufactures, and original suppliers can create an account to buy, sell, or donate materials</li>
    <li style="top:599px"><svg><use href="#tick-box"/></svg>Part 11 compliant signature and authentication</li>
    <li style="top:637px"><svg><use href="#tick-box"/></svg>Leverages industry auditing skills to facilitate compliant and transparent transactions</li>
    <li style="top:675px"><svg><use href="#tick-box"/></svg>Some of the best and industry vendors and software used</li>
  </ul>

  <div class="section-tag tag-benefits">BENEFITS</div>
  <ul class="checklist">
    <li style="top:778px"><svg><use href="#tick-box"/></svg>Reduce write-offs by selling excess and obsolete materials, equipment, spare parts, etc.</li>
    <li style="top:816px"><svg><use href="#tick-box"/></svg>Buy quality materials at a reduced price.</li>
    <li style="top:854px"><svg><use href="#tick-box"/></svg>Market materials if an original supplier</li>
    <li style="top:891px"><svg><use href="#tick-box"/></svg>Donate material to researchers</li>
    <li style="top:929px"><svg><use href="#tick-box"/></svg>Acquire donated materials</li>
    <li style="top:967px"><svg><use href="#tick-box"/></svg>Collaborate and consort to reduce supply chain risk such as mutual aid agreements, joint supplier audits, etc.</li>
  </ul>

  <div class="section-tag tag-promise">OUR PROMISE</div>
  <ul class="checklist">
    <li style="top:1067px"><svg><use href="#tick-box"/></svg>A greener, more cost-efficient, and quality driven supply chain through a collaborative life sciences marketplace.</li>
  </ul>

  <footer class="footer">
    <span class="footer-item">
      <svg viewBox="0 0 13 13"><rect x="1" y="3" width="11" height="7" fill="#fff"/><path d="M1 3 L6.5 7 L12 3" fill="none" stroke="#0b5aa3" stroke-width="1"/></svg>
      info@telvamoreqx.com
    </span>
    <span class="footer-item">
      <svg viewBox="0 0 13 13"><path d="M6.5 1 A3.5 3.5 0 0 1 10 4.5 C10 7 6.5 12 6.5 12 C6.5 12 3 7 3 4.5 A3.5 3.5 0 0 1 6.5 1Z" fill="#fff"/><circle cx="6.5" cy="4.5" r="1.3" fill="#0b5aa3"/></svg>
      www.telvamoreqx.com
    </span>
    <span class="footer-item">
      <svg viewBox="0 0 13 13"><rect x="1" y="3" width="11" height="8" fill="none" stroke="#fff" stroke-width="1.4"/><line x1="6.5" y1="3" x2="6.5" y2="11" stroke="#fff" stroke-width="1.2"/></svg>
      white paper
    </span>
  </footer>
</body>
</html>
```